Tallowreed Advisory Partners Business Card Design

We have the logo we just need someone to design a modern business card design.

Name: Desmond Munkalt
Phone: 3055550148
Mobile: 9175550193
Web:www.tallowreedadvisory.example
email: dmunkalt@tallowreedadvisory.example
Company: Tallowreed Advisory Partners
Title: CEO

Address: 718 Quillmore Ave, Miami, Florida 33190

Target Market(s)

companies over 100 employees

Industry/Entity Type

Business

```html
<!DOCTYPE html>
<html lang="en">
<head>
<meta charset="utf-8">
<title>Tallowreed Advisory Partners – Business Card</title>
<link rel="stylesheet" href="https://fonts.googleapis.com/css2?family=Archivo:wdth,wght@62..125,700&display=swap">
<style>
  :root {
    --card-black: #000000;
    --brand-blue: #0070b8;
    --rule-white: #ffffff;
    --name-white: #ffffff;
  }
  html, body {
    margin: 0;
    padding: 0;
    width: 1200px;
    height: 686px;
    overflow: hidden;
    background: var(--card-black);
  }
  .card {
    position: relative;
    width: 1200px;
    height: 686px;
    background: var(--card-black);
    overflow: hidden;
    font-family: "Archivo", "Helvetica Neue", Arial, sans-serif;
  }
  .brand-dot {
    position: absolute;
    left: 490px;
    top: 109px;
    width: 274px;
    height: 274px;
  }
  .company-name {
    position: absolute;
    left: 0;
    width: 1256px;
    margin: 0;
    text-align: center;
    color: var(--name-white);
    font-weight: 700;
    font-stretch: 125%;
    line-height: 1;
    text-transform: uppercase;
  }
  .company-name__main {
    top: 440px;
    font-size: 86px;
    letter-spacing: 1px;
  }
  .company-name__sub {
    top: 530px;
    font-size: 29px;
    letter-spacing: 1.5px;
  }
  .rule-white {
    position: absolute;
    left: 0;
    top: 607px;
    width: 1200px;
    height: 17px;
    background: var(--rule-white);
  }
  .band-blue {
    position: absolute;
    left: 0;
    top: 624px;
    width: 1200px;
    height: 62px;
    background: var(--brand-blue);
  }
</style>
</head>
<body>
  <main class="card">
    <svg class="brand-dot" viewBox="0 0 274 274" aria-hidden="true">
      <circle cx="137" cy="137" r="137" fill="var(--brand-blue)"/>
    </svg>
    <h1 class="company-name company-name__main">Tallowreed</h1>
    <p class="company-name company-name__sub">Advisory Partners</p>
    <div class="rule-white"></div>
    <div class="band-blue"></div>
  </main>
</body>
</html>
```